(4) Bowling League Designs 1920x1080

Will be used on our website and in some digital signage.

We are starting (4) leagues this summer and need a basic graphic as an attention grab which will then lead the customer to full information / sign ups. The information I would need on each one is as follows:

1. Monday Night FREE ball league - Begins May 3rd

2. Tuesday Trios - KFDL Sanctioned - Begins May 11th
$9,000 prize fund

3. Wednesday Cosmic League - 9 pin no tap fun league - May 12th start

4. Thursday Night FREE ball league - Begins May 13th

I will attach some random examples of previous ones to give you an idea.

```html
<!DOCTYPE html>
<html lang="en">
<head>
<meta charset="UTF-8">
<title>Thursday Night Free Ball League</title>
<link rel="stylesheet" href="https://fonts.googleapis.com/css2?family=Barlow+Condensed:ital,wght@1,600;1,700;1,800&display=swap">
<style>
  :root {
    --ink: #050403;
    --gold: #ffe14d;
    --gold-deep: #b8901c;
    --amber: #6e5410;
    --ivory: #f3e7c8;
    --white: #ffffff;
    --glow: rgba(255, 214, 80, 0.85);
  }
  * { margin: 0; padding: 0; box-sizing: border-box; }
  html, body { width: 1200px; height: 675px; overflow: hidden; background: var(--ink); }
  .poster {
    position: relative; width: 1200px; height: 675px; overflow: hidden;
    background:
      radial-gradient(ellipse 300px 200px at 330px 330px, rgba(255, 200, 60, 0.22) 0%, transparent 70%),
      linear-gradient(100deg, var(--ink) 0%, #140f04 28%, #3a2c08 45%, var(--amber) 60%, #2a2006 100%);
    font-family: "Barlow Condensed", "Arial Narrow", sans-serif;
  }
  .hero-art {
    position: absolute; left: 430px; top: 0; width: 770px; height: 675px;
    background:
      radial-gradient(ellipse 200px 190px at 610px 500px, rgba(30, 26, 18, 0.85) 0%, rgba(30, 26, 18, 0.5) 55%, transparent 85%),
      radial-gradient(ellipse 380px 230px at 450px 300px, rgba(243, 231, 200, 0.75) 0%, rgba(243, 231, 200, 0.35) 45%, transparent 75%),
      radial-gradient(ellipse 500px 420px at 420px 200px, rgba(255, 215, 90, 0.45) 0%, transparent 75%),
      linear-gradient(180deg, #4a3a0c 0%, #9a7818 50%, #5a460e 100%);
    -webkit-mask-image: linear-gradient(90deg, transparent 0%, #000 30%);
            mask-image: linear-gradient(90deg, transparent 0%, #000 30%);
  }
  .shapes { position: absolute; inset: 0; }
  .headline {
    position: absolute; font-style: italic; font-weight: 800; line-height: 1;
    text-transform: uppercase;
  }
  .headline--day { left: 98px; top: 46px; font-size: 84px; letter-spacing: 3.5px; color: var(--gold); }
  .headline--night { left: 95px; top: 120px; font-size: 84px; letter-spacing: 4.5px; color: var(--white); }
  .league { position: absolute; font-style: italic; font-weight: 800; line-height: 1; color: var(--white); }
  .league--bal { left: 92px; top: 422px; font-size: 80px; letter-spacing: 4px; }
  .league--l { left: 206px; top: 410px; font-size: 140px; color: var(--gold); font-weight: 700; }
  .league--eague { left: 258px; top: 451px; font-size: 86px; letter-spacing: 5px; }
  .start-date {
    position: absolute; left: 75px; top: 558px; width: 388px; height: 58px;
    display: flex; align-items: center; justify-content: center;
    font-style: italic; font-weight: 600; font-size: 40px; color: var(--white);
    text-shadow: 0 0 6px var(--glow);
  }
</style>
</head>
<body>
<main class="poster">
  <div class="hero-art" role="img" aria-label="Black bowling ball crashing into white pins with red stripes under golden light rays and sparkles"></div>

  <svg class="shapes" width="1200" height="675" viewBox="0 0 1200 675" aria-hidden="true">
    <defs>
      <filter id="neon" x="-20%" y="-20%" width="140%" height="140%">
        <feGaussianBlur stdDeviation="4" result="b"/>
        <feMerge><feMergeNode in="b"/><feMergeNode in="SourceGraphic"/></feMerge>
      </filter>
    </defs>
    <polygon points="36,66 78,84 36,103 48,84" fill="var(--gold)"/>
    <polygon points="36,431 78,452 36,475 48,452" fill="var(--gold)"/>

    <g fill="none">
      <polygon points="22,188 538,188 506,419 12,419" stroke="rgba(255,255,255,0.18)" stroke-width="2"/>
      <polygon points="42,200 516,200 490,408 32,408" stroke="rgba(255,255,255,0.25)" stroke-width="2"/>
      <polygon points="66,212 494,212 468,398 56,398" stroke="rgba(255,255,255,0.4)" stroke-width="3"/>
      <polygon points="82,225 475,225 450,394 75,394" fill="rgba(20,14,2,0.55)" stroke="var(--white)" stroke-width="3" filter="url(#neon)"/>
    </g>
    <text x="270" y="368" text-anchor="middle" font-family="Barlow Condensed, sans-serif" font-style="italic" font-weight="800" font-size="165" letter-spacing="4" fill="none" stroke="var(--white)" stroke-width="4" filter="url(#neon)">FREE</text>

    <rect x="275" y="442" width="370" height="4" fill="var(--gold)"/>
    <rect x="0" y="504" width="178" height="4" fill="var(--gold)"/>

    <g fill="rgba(20,14,2,0.4)" stroke="var(--white)" stroke-width="2.5" filter="url(#neon)">
      <polygon points="80,558 463,558 458,616 75,616"/>
      <polygon points="475,558 503,558 498,616 470,616"/>
      <polygon points="516,558 546,558 541,616 511,616"/>
      <polygon points="558,558 588,558 583,616 553,616"/>
    </g>
  </svg>

  <h1 class="headline headline--day">Thursday</h1>
  <p class="headline headline--night">Night</p>
  <p class="league league--bal">BAL</p>
  <p class="league league--l">L</p>
  <p class="league league--eague">EAGUE</p>
  <p class="start-date">Begins May 13th</p>
</main>
</body>
</html>
```